Regional and National Rugby Training and Player Development Company

We need a new responsive website design that is easy to navigate and encourages people to register for our programs.

Registration and payment could be written into the site but it can also be externally integrated as it is currently.

I want clean lines, bright images, and a webpage that is easy to update and manage. Currently using WordPress.
Updates

Ferncrest Rugby runs four programs:  Junior Sunfield Rugby Clinics, Frostline Court Tag Rugby, Bloomtide Skills Clinics, and the "Athlete Growth Pathway" otherwise known as the Forge

Ultimately, Ferncrest Rugby wants to attract the top players across the province of Ontario to join our corner-stone program, the Frostline Forge.

We have had many players play at the provincial level and a select handful go on to represent Canada.  We aspire to set the standard for off-season junior rugby player development.

Reason: 1) Laptop crashed on Thurs. which meant I couldn't make a fair decision this weekend. 2). There are FIVE very good designs, each somewhat unique. I want to see what designers come up with when I outline what I like in each as a requirement of what has been provided. Thank you for your understanding and efforts in this regard. Sincerely, MB Sent from my iPad

Thank you for all your efforts and patience in this design campaign, I truly appreciate it.  Apologies for the lack of communication but as a full-time high school teacher, sometimes my "real job" gets put to the side.  

I have reduced over 30 designs to five... you are the five remaining I hope to take certain aspects of each that I like best and provide some feedback to you the designers, in order to make final adjustments before my final decision.

I hope you find this process agreeable and again, thank you for your patience and efforts in this campaign.  I think each of your designs look fantastic and are a drastic and valuable improvement of what I have been using up to this point.

Appreciatively,

MB

Voting poll results are in and there are three distinct leaders... going to focus on these three this week and come to a final decision before Friday.

Each designer will be contacted privately to provide some feedback and see what the best final product can look like.

Thank you for your patience and high-quality work!

MB

Reason: Just too much going on at the moment and trying to stay on top of this. Apologies to all. Just had the results of the voting poll come in and have reduced choices to two clear leaders with a third alternate. Going to provide feedback for all three today and hope to make final decision by Friday. Thank you for your efforts.

Target Market(s)

Junior rugby players (boys and girls) between the ages of 12 and 20... more importantly, their parents!

Requirements
Must have
• Must have high-resolution, clean lines, and encourage registration in programs. I would like it to be integrated with my YouTube page as well as other social media.

```html
<!DOCTYPE html>
<html lang="en">
<head>
<meta charset="utf-8">
<title>Ferncrest Rugby Canada</title>
<link href="https://fonts.googleapis.com/css2?family=Lato:wght@300;400;700&family=Ubuntu:wght@500;700&display=swap" rel="stylesheet">
<style>
:root{
  --red:#d3232b;
  --ink:#333;
  --body:#6b6b6b;
  --muted:#8a8a8a;
  --line:#e3e3e3;
  --footer:#262324;
  --footer-base:#141213;
  --white:#fff;
}
*{margin:0;padding:0;box-sizing:border-box}
html,body{width:818px;height:1200px;overflow:hidden;background:var(--white)}
body{position:relative;font-family:"Lato",sans-serif;color:var(--ink)}
.abs{position:absolute}

/* header */
.site-header{left:0;top:0;width:818px;height:64px;background:var(--white)}
.brand{left:137px;top:0;width:166px;height:98px;background:var(--white);border-radius:0 0 50% 50%/0 0 28px 28px;z-index:3;display:flex;flex-direction:column;align-items:center;justify-content:flex-end;padding-bottom:9px;box-shadow:0 2px 3px rgba(0,0,0,.15)}
.brand-mark{width:24px;height:24px;background:var(--red);border-radius:50%;margin-bottom:10px}
.brand-name{font-family:"Ubuntu",sans-serif;font-weight:700;color:var(--red);font-size:15px;line-height:17px;text-align:center;text-transform:uppercase;letter-spacing:.3px}
.search{left:545px;top:14px;display:flex}
.search-input{width:101px;height:14px;border:1px solid #ddd;font-size:6px;color:#bbb;font-style:italic;padding:3px 5px;line-height:8px}
.search-btn{width:35px;height:14px;background:var(--red);color:var(--white);font-size:7.5px;font-weight:700;text-align:center;line-height:14px}
.main-nav{left:430px;top:36px;display:flex;font-size:7.5px;color:var(--muted)}
.main-nav span{padding:0 9px;border-left:1px solid #ddd;line-height:9px}
.main-nav span:first-child{border-left:0}

/* hero */
.hero{left:0;top:64px;width:818px;height:344px;background:
  linear-gradient(180deg,#6b5a52 0%,#8a7468 12%,#5d4f55 24%,#5a4a8c 30%,#4f7a3c 40%,#7fa23e 55%,#93b44a 72%,#86a640 88%,#6f8e34 100%)}
.social{left:792px;top:104px;width:26px;height:106px;background:var(--white);border-radius:3px 0 0 3px;box-shadow:0 0 3px rgba(0,0,0,.3);display:flex;flex-direction:column;align-items:center;gap:7px;padding-top:6px;z-index:3}
.social i{display:block;width:13px;height:13px;border-radius:2px}
.hero-copy{left:137px;top:183px;width:460px;height:66px;background:rgba(20,20,20,.45);text-align:center;padding-top:2px}
.hero-title{font-family:"Ubuntu",sans-serif;font-weight:700;font-size:38px;line-height:42px;color:var(--white);letter-spacing:-.5px}
.hero-title em{font-style:normal;color:var(--red)}
.hero-sub{font-weight:300;font-size:17.5px;color:var(--white);line-height:20px}
.btn{font-family:"Ubuntu",sans-serif;font-weight:500;font-size:19px;color:var(--white);height:34px;line-height:32px;text-align:center}
.btn-register{left:137px;top:288px;width:129px;background:var(--red);box-shadow:0 2px 2px rgba(0,0,0,.3)}
.btn-learn{left:274px;top:288px;width:115px;border:1.5px solid var(--white);background:rgba(0,0,0,.35)}

/* programs */
.section-title{left:136px;top:425px;font-weight:700;font-size:21px;color:#222}
.program-title{font-size:11px;color:#555}
.program-photo{width:147px;height:98px;border:3px solid #c9c9c9}
.program-text{width:385px;font-size:7.9px;line-height:11px;color:var(--body)}
.more{width:38px;height:15px;background:var(--red);color:var(--white);font-size:7px;font-weight:700;line-height:15px;text-align:center}
.divider{left:136px;width:546px;height:0;border-top:1px dashed var(--line)}

/* footer */
.site-footer{left:0;top:1079px;width:818px;height:99px;background:var(--footer)}
.footer-mark{left:399px;top:1095px;width:20px;height:20px;border-radius:50%;background:#6f6b6c}
.footer-name{left:0;top:1127px;width:818px;text-align:center;font-family:"Ubuntu",sans-serif;font-weight:500;font-size:9px;line-height:11px;letter-spacing:1px;color:#7b7778;text-transform:uppercase}
.footer-nav{left:0;top:1160px;width:818px;display:flex;justify-content:center;font-size:7.5px;color:#6b6768}
.footer-nav span{padding:0 9px;border-left:1px solid #4a4647;line-height:9px}
.footer-nav span:first-child{border-left:0}
.footer-base{left:0;top:1178px;width:818px;height:22px;background:var(--footer-base);color:#6b6768;font-size:6px;line-height:22px;text-align:center}
</style>
</head>
<body>

<header class="abs site-header">
  <div class="abs brand"><span class="brand-mark"></span><div class="brand-name">Ferncrest Rugby<br>Canada</div></div>
  <div class="abs search"><div class="search-input">Enter your key words...</div><div class="search-btn">Search</div></div>
  <nav class="abs main-nav"><span>Home</span><span>About Us</span><span>Services</span><span>Community</span><span>Contact Us</span></nav>
</header>

<section class="abs hero" role="img" aria-label="Photo of a rugby scrum on bright turf in front of a stadium crowd"></section>
<div class="abs social">
  <i style="background:#3b5998"></i><i style="background:#2a9fd6"></i><i style="background:#d34836"></i><i style="background:#c4302b"></i><i style="background:#4a7ba6"></i>
</div>
<div class="abs hero-copy">
  <div class="hero-title">Our <em>Mission</em> Is To Develop</div>
  <div class="hero-sub">Young Players Within An Environment That Is Challenging</div>
</div>
<div class="abs btn btn-register">Register Now</div>
<div class="abs btn btn-learn">Learn More</div>

<h2 class="abs section-title">PROGRAMS!</h2>

<div class="abs program-title" style="left:136px;top:462px">Junior Sunfield Rugby Clinics</div>
<div class="abs program-photo" style="left:137px;top:482px;background:linear-gradient(180deg,#3d8fe6 0%,#8cc4f2 30%,#c9d3da 45%,#7a7a72 58%,#62b83a 78%,#74cc44 100%)" role="img" aria-label="Group photo of junior players outside a campus building"></div>
<p class="abs program-text" style="left:292px;top:483px">Lorem ipsum dolor sit amet, consectetur adipiscing elit. Vivamus mollis et ligula eget viverra. Vestibulum sit amet posuere neque. Donec id ante metus. Proin scelerisque, tellus vitae gravida commodo, mauris erat interdum arcu, id aliquet dolor mauris eget nisi.<br>Nunc condimentum ornare nisl, sed adipiscing eros vehicula ac. Phasellus vel nulla risus. Donec bibendum elit ut orci luctus, eget iaculis arcu auctor.</p>
<div class="abs more" style="left:292px;top:563px">More...</div>
<div class="abs divider" style="top:602px"></div>

<div class="abs program-title" style="left:534px;top:622px">Frostline Court Tag Rugby</div>
<div class="abs program-photo" style="left:534px;top:641px;background:linear-gradient(160deg,#f0cf78 0%,#e2b85a 45%,#d4a648 75%,#e8c46a 100%)" role="img" aria-label="Players on a bright indoor gym court"></div>
<p class="abs program-text" style="left:136px;top:642px">Lorem ipsum dolor sit amet, consectetur adipiscing elit. Vivamus mollis et ligula eget viverra. Vestibulum sit amet posuere neque. Donec id ante metus. Proin scelerisque, tellus vitae gravida commodo, mauris erat interdum arcu, id aliquet dolor mauris eget nisi.<br>Nunc condimentum ornare nisl, sed adipiscing eros vehicula ac. Phasellus vel nulla risus. Donec bibendum elit ut orci luctus, eget iaculis arcu auctor.</p>
<div class="abs more" style="left:137px;top:722px">More...</div>
<div class="abs divider" style="top:762px"></div>

<div class="abs program-title" style="left:136px;top:780px">Bloomtide Skills Clinics</div>
<div class="abs program-photo" style="left:137px;top:800px;background:linear-gradient(180deg,#a8b894 0%,#2f6fe0 28%,#3a7ef0 55%,#5db83a 75%,#6ccc44 100%)" role="img" aria-label="Players in blue jerseys doing drills on grass"></div>
<p class="abs program-text" style="left:292px;top:801px">Lorem ipsum dolor sit amet, consectetur adipiscing elit. Vivamus mollis et ligula eget viverra. Vestibulum sit amet posuere neque. Donec id ante metus. Proin scelerisque, tellus vitae gravida commodo, mauris erat interdum arcu, id aliquet dolor mauris eget nisi.<br>Nunc condimentum ornare nisl, sed adipiscing eros vehicula ac. Phasellus vel nulla risus. Donec bibendum elit ut orci luctus, eget iaculis arcu auctor.</p>
<div class="abs more" style="left:292px;top:880px">More...</div>
<div class="abs divider" style="top:920px"></div>

<div class="abs program-title" style="left:534px;top:939px">Athlete Growth Pathway</div>
<div class="abs program-photo" style="left:534px;top:958px;background:linear-gradient(180deg,#eef3f7 0%,#d6e4ec 18%,#4f8f3a 34%,#7cc046 55%,#f2c230 72%,#6cb43e 86%,#5aa234 100%)" role="img" aria-label="Coach leading players in yellow through a field drill"></div>
<p class="abs program-text" style="left:136px;top:959px">Lorem ipsum dolor sit amet, consectetur adipiscing elit. Vivamus mollis et ligula eget viverra. Vestibulum sit amet posuere neque. Donec id ante metus. Proin scelerisque, tellus vitae gravida commodo, mauris erat interdum arcu, id aliquet dolor mauris eget nisi.<br>Nunc condimentum ornare nisl, sed adipiscing eros vehicula ac. Phasellus vel nulla risus. Donec bibendum elit ut orci luctus, eget iaculis arcu auctor.</p>
<div class="abs more" style="left:137px;top:1039px">More...</div>

<footer>
  <div class="abs site-footer"></div>
  <div class="abs footer-mark"></div>
  <div class="abs footer-name">Ferncrest Rugby<br>Canada</div>
  <nav class="abs footer-nav"><span>Home</span><span>About Us</span><span>Services</span><span>Community</span><span>Contact Us</span></nav>
  <div class="abs footer-base">FERNCREST RUGBY CANADA © 2013 . All rights reserved &nbsp;|&nbsp; Privacy Policy &nbsp;|&nbsp; Terms &amp; Conditions</div>
</footer>

</body>
</html>
```